Step and Repeat Backdrop for wedding reception photo booth

Would like to have a Step and Repeat Backdrop (8 foot high by 10 foot wide) that incorporates the wedding logo (attached) and the names Clara and Bruno. Background should be white, and wedding colors are burgundy and gold. Show me creativity :-) I have included some random samples.

```html
<!DOCTYPE html>
<html lang="en">
<head>
<meta charset="utf-8">
<title>Clara and Bruno — Step and Repeat Backdrop</title>
<link rel="stylesheet" href="https://fonts.googleapis.com/css2?family=Cinzel:wght@400;600&display=swap">
<style>
  :root {
    --page: #f3f3f3;
    --backdrop: #ffffff;
    --gold: #d4a52c;
    --copper: #c46d2c;
    --burgundy: #9b1b30;
  }
  html, body {
    margin: 0;
    width: 1200px;
    height: 2365px;
    overflow: hidden;
    background: var(--page);
  }
  .backdrop {
    position: absolute;
    left: 0;
    top: 722px;
    width: 1200px;
    height: 920px;
    background: var(--backdrop);
    font-family: "Cinzel", serif;
  }
  .tile {
    position: absolute;
    display: flex;
    align-items: center;
  }
  .tile-mark {
    width: 80px;
    height: 60px;
    display: flex;
    flex-direction: column;
    align-items: center;
    justify-content: center;
    color: var(--gold);
    font-weight: 600;
    font-size: 13px;
    line-height: 1.1;
    text-align: center;
  }
  .tile-name,
  .tile-name-solo {
    margin-left: 40px;
    color: var(--gold);
    font-weight: 600;
    font-size: 11px;
    letter-spacing: 0.2px;
    white-space: nowrap;
  }
  .tile-name-solo {
    position: absolute;
    margin: 0;
    transform: translateY(-50%);
  }
  .ornament {
    position: absolute;
    left: 372px;
    width: 447px;
    border-radius: 60px;
  }
  .ornament-top {
    top: 174px;
    height: 132px;
    background: linear-gradient(90deg, var(--gold), #e2bd4a 50%, var(--gold));
    opacity: 0.55;
  }
  .ornament-bottom {
    top: 497px;
    height: 140px;
    background: linear-gradient(90deg, var(--burgundy), var(--copper) 70%, #d48a3a);
    opacity: 0.55;
  }
  .feature-mark {
    position: absolute;
    left: 422px;
    top: 306px;
    width: 356px;
    height: 182px;
    display: flex;
    flex-direction: column;
    align-items: center;
    justify-content: center;
    color: var(--copper);
    font-weight: 600;
    font-size: 64px;
    line-height: 1.05;
  }
  .feature-name {
    position: absolute;
    left: 0;
    width: 1200px;
    top: 640px;
    text-align: center;
    color: var(--burgundy);
    font-weight: 400;
    font-size: 58px;
    letter-spacing: 1px;
    margin: 0;
  }
</style>
</head>
<body>
<main class="backdrop">
  <!-- row 1 -->
  <div class="tile" style="left:51px;top:28px"><div class="tile-mark"><span>Clara &amp;</span><span>Bruno</span></div><span class="tile-name">CLARA AND BRUNO</span></div>
  <div class="tile" style="left:486px;top:28px"><div class="tile-mark"><span>Clara &amp;</span><span>Bruno</span></div><span class="tile-name">CLARA AND BRUNO</span></div>
  <div class="tile" style="left:917px;top:28px"><div class="tile-mark"><span>Clara &amp;</span><span>Bruno</span></div><span class="tile-name">CLARA AND BRUNO</span></div>
  <!-- row 2 -->
  <div class="tile" style="left:269px;top:130px"><div class="tile-mark"><span>Clara &amp;</span><span>Bruno</span></div><span class="tile-name">CLARA AND BRUNO</span></div>
  <div class="tile" style="left:701px;top:130px"><div class="tile-mark"><span>Clara &amp;</span><span>Bruno</span></div><span class="tile-name">CLARA AND BRUNO</span></div>
  <!-- row 3 -->
  <div class="tile" style="left:51px;top:230px"><div class="tile-mark"><span>Clara &amp;</span><span>Bruno</span></div><span class="tile-name">CLARA AND BRUNO</span></div>
  <div class="tile" style="left:917px;top:230px"><div class="tile-mark"><span>Clara &amp;</span><span>Bruno</span></div><span class="tile-name">CLARA AND BRUNO</span></div>
  <!-- row 4 -->
  <div class="tile" style="left:269px;top:329px"><div class="tile-mark"><span>Clara &amp;</span><span>Bruno</span></div></div>
  <span class="tile-name-solo" style="left:821px;top:359px">CLARA AND BRUNO</span>
  <!-- row 5 -->
  <div class="tile" style="left:51px;top:428px"><div class="tile-mark"><span>Clara &amp;</span><span>Bruno</span></div><span class="tile-name">CLARA AND BRUNO</span></div>
  <div class="tile" style="left:917px;top:428px"><div class="tile-mark"><span>Clara &amp;</span><span>Bruno</span></div><span class="tile-name">CLARA AND BRUNO</span></div>
  <!-- row 6 -->
  <div class="tile" style="left:269px;top:528px"><div class="tile-mark"><span>Clara &amp;</span><span>Bruno</span></div></div>
  <span class="tile-name-solo" style="left:821px;top:558px">CLARA AND BRUNO</span>
  <!-- row 7 -->
  <div class="tile" style="left:51px;top:627px"><div class="tile-mark"><span>Clara &amp;</span><span>Bruno</span></div><span class="tile-name">CLARA AND BRUNO</span></div>
  <div class="tile" style="left:917px;top:627px"><div class="tile-mark"><span>Clara &amp;</span><span>Bruno</span></div><span class="tile-name">CLARA AND BRUNO</span></div>
  <!-- row 8 -->
  <div class="tile" style="left:269px;top:726px"><div class="tile-mark"><span>Clara &amp;</span><span>Bruno</span></div><span class="tile-name">CLARA AND BRUNO</span></div>
  <div class="tile" style="left:701px;top:726px"><div class="tile-mark"><span>Clara &amp;</span><span>Bruno</span></div><span class="tile-name">CLARA AND BRUNO</span></div>
  <!-- row 9 -->
  <div class="tile" style="left:51px;top:826px"><div class="tile-mark"><span>Clara &amp;</span><span>Bruno</span></div><span class="tile-name">CLARA AND BRUNO</span></div>
  <div class="tile" style="left:486px;top:826px"><div class="tile-mark"><span>Clara &amp;</span><span>Bruno</span></div><span class="tile-name">CLARA AND BRUNO</span></div>
  <div class="tile" style="left:917px;top:826px"><div class="tile-mark"><span>Clara &amp;</span><span>Bruno</span></div><span class="tile-name">CLARA AND BRUNO</span></div>

  <!-- central feature -->
  <div class="ornament ornament-top" role="img" aria-label="Gold scrollwork ornament with fleur-de-lis"></div>
  <div class="feature-mark"><span>Clara</span><span>&amp; Bruno</span></div>
  <div class="ornament ornament-bottom" role="img" aria-label="Burgundy scrollwork ornament with pendant"></div>
  <h1 class="feature-name">CLARA AND BRUNO</h1>
</main>
</body>
</html>
```